Ferrolix - Train Delay Compensation. We help cummuters in the uk using national rail get there money

We help train commuter who pay very high price for their rail ticket.on Weekly, Monthly and yearly ticket) get some of their money back when their train is delayed or cancelled up to a max of £300 per month all they need to do is download our app from the app store app or android of visit our website www.ferrolix-example.com . The get back up to 40% the cost of their ticket . No claim no fee!! Unlimited claims !! No form filling , No printing no posting we do all the work just claim and wait for your money through the post.
Task
A6 Size paper design and wordings over the 2 pages front and back . wording should include high impact words like ' Don't be short changed ' ' It's your money get it back!! ' The big deal Get up to 40% of cost of ticket back' ' No claim no fee!' preferable should include on the front page picture of crowd of people packed tight on the train or stuck at a train station. Uk Pictures only please . I have a vector image of the logo of out company if needed will upload a jpeg now

with our app they will get possible claim notifications when their trains is late and they are in line for a compensation which can be between 50% to 100% the cost of a daily ticket

Target Market(s)

train commuter in the uk

Requirements
Must have
• No claim no fee.,The big deal Get up to 40% of cost of ticket back' max of £300 per month. Don't be short changed get it's your money get it back. download out app and we do the rest free trial ! . No filling forms , printing or posting of forms we do all the work for you. Just click claim and wait for your money thorough the post. No claim no fee!! Unlimited claims !! No form filling , No printing no posting we do all the work just claim and wait for your money through the post.
• Logo of the company. Must be high impact and attention grabbing !!
Nice to have
• Pictures of commuters packed in the train. Picture of commuters stranded at the train station because of delayed or cancelled trains.

```html
<!DOCTYPE html>
<html lang="en">
<head>
<meta charset="utf-8">
<title>Ferrolix – Train Delay Compensation Flyer</title>
<link rel="stylesheet" href="https://fonts.googleapis.com/css2?family=Anton&family=Arimo:ital,wght@0,400;0,700;1,700&display=swap">
<style>
  :root{
    --navy:#1b2a6b;
    --navy-deep:#13205a;
    --blue:#1f3fa8;
    --red:#c8102e;
    --red-dark:#9e0b22;
    --orange:#f47b20;
    --white:#ffffff;
    --ink:#1a1a2e;
    --paper-bg:#e8e6e2;
    --photo-a:#6d5b52;
    --photo-b:#2d3340;
    --photo-c:#9aa2ad;
  }
  *{margin:0;padding:0;box-sizing:border-box}
  html,body{width:1200px;height:800px;overflow:hidden}
  body{background:var(--paper-bg);position:relative;font-family:"Arimo",Arial,sans-serif;color:var(--ink)}

  .page{position:absolute;top:38px;width:508px;height:725px;background:var(--white);overflow:hidden;box-shadow:0 4px 14px rgba(0,0,0,.25)}
  .page--front{left:80px}
  .page--back{left:624px}
  .page svg.shapes{position:absolute;inset:0}
  .abs{position:absolute}

  /* ---------- front ---------- */
  .corner-ribbon-text{left:-24px;top:55px;width:180px;height:22px;line-height:22px;transform:rotate(-45deg);transform-origin:center;color:var(--white);font-weight:700;font-size:17px;text-align:center;white-space:nowrap}
  .cap-block{left:56px;top:104px;line-height:1}
  .cap-block .small{font-size:15px;font-weight:700;letter-spacing:-.5px}
  .cap-block .amount{font-size:32px;font-weight:700;color:var(--red);letter-spacing:-1.5px;line-height:1.05}
  .cap-block .tickets{font-size:15px;letter-spacing:-.6px;line-height:1.05;margin-top:4px}

  .brand{left:212px;top:28px;width:156px;text-align:center}
  .brand-dot{width:62px;height:62px;border-radius:50%;background:var(--red);margin:0 auto 14px}
  .brand-name{font-weight:700;font-size:29px;color:var(--red);letter-spacing:1px}

  .headline{left:32px;top:256px;font-family:"Anton",Impact,sans-serif;font-style:italic;font-size:46px;line-height:1;color:var(--navy);transform:rotate(-20.5deg);transform-origin:left bottom;white-space:nowrap;letter-spacing:.5px}
  .band-line{left:34px;top:340px;font-weight:700;font-style:italic;font-size:23px;line-height:1;color:var(--white);transform:rotate(-22deg);transform-origin:left bottom;white-space:nowrap}

  .deal-badge{left:26px;top:572px;width:156px;height:156px;border-radius:50%;background:var(--navy);border:8px solid var(--white);color:var(--white);text-align:center;padding-top:22px;line-height:1}
  .deal-badge .title{color:var(--orange);font-weight:700;font-size:14px;letter-spacing:-.5px}
  .deal-badge .sub{font-size:11px;font-weight:700;margin-top:2px}
  .deal-badge .pct{color:var(--orange);font-weight:700;font-size:50px;letter-spacing:-3px;margin:1px 0}
  .deal-badge .pct span{font-size:26px;letter-spacing:0}
  .deal-badge .tail{font-size:10px;font-weight:700;line-height:1.3}

  .comp-head{left:334px;top:572px;color:var(--white);font-size:17px;line-height:.98;letter-spacing:-.6px}
  .comp-head b{font-weight:700}
  .comp-box{top:614px;width:72px;height:68px;background:var(--red);border:3px solid var(--white);border-radius:4px;color:var(--white);font-weight:700;font-size:30px;letter-spacing:-2px;display:flex;align-items:center;justify-content:center}
  .comp-box small{font-size:13px;letter-spacing:0;margin-top:8px}
  .comp-box--low{left:284px}
  .comp-box--high{left:400px}
  .comp-to{left:366px;top:632px;width:34px;text-align:center;color:var(--white);font-weight:700;font-size:22px}
  .comp-foot{left:282px;top:692px;color:var(--white);font-weight:700;font-size:17px;letter-spacing:-.6px}

  /* ---------- back ---------- */
  .back-headline{left:40px;top:30px;color:var(--red);font-weight:700;font-size:26px;line-height:1.03;letter-spacing:-1.4px;white-space:nowrap}
  .speech{left:40px;top:120px;width:296px;background:var(--white);border-radius:4px;box-shadow:0 2px 6px rgba(0,0,0,.3);padding:4px 6px;font-size:15px;font-weight:700;color:var(--navy);line-height:1.55;letter-spacing:-.4px;white-space:nowrap}
  .speech em{font-style:normal;color:var(--red)}
  .band-copy{left:38px;top:254px;color:var(--white);font-weight:700;font-size:15px;letter-spacing:-.3px}

  .perk{width:84px;height:84px;border-radius:50%;background:var(--blue);border:4px solid var(--white);box-shadow:0 2px 4px rgba(0,0,0,.3);color:var(--white);font-weight:700;font-size:13.5px;line-height:1.1;display:flex;align-items:center;justify-content:center;text-align:center;letter-spacing:-.3px}

  .closing{left:26px;top:560px;color:var(--navy);font-weight:700;font-size:17px;line-height:1.2;letter-spacing:-.4px;white-space:nowrap}
  .how-to{left:26px;top:612px;font-size:11px;line-height:1.2;letter-spacing:-.3px;color:var(--ink)}
  .how-to a{color:var(--red);font-weight:700;text-decoration:none}
  .store-slot{top:660px;height:25px;border-radius:3px}
  .store-slot--ios{left:28px;width:76px;background:#111}
  .store-slot--android{left:110px;width:84px;background:#8cc63f;border:1px solid #6aa52a}

  .brand-small{left:350px;top:590px;width:130px;text-align:center}
  .brand-small .brand-dot{width:54px;height:54px;margin-bottom:10px}
  .brand-small .brand-name{font-size:24px}
</style>
</head>
<body>

<section class="page page--front">
  <svg class="shapes" width="508" height="725" viewBox="0 0 508 725">
    <defs>
      <linearGradient id="frontTop" x1="0" y1="0" x2="0" y2="1">
        <stop offset="0" stop-color="#ffffff"/><stop offset="1" stop-color="#e6e7eb"/>
      </linearGradient>
      <linearGradient id="trainCrowd" x1="0" y1="0" x2="1" y2="1">
        <stop offset="0" stop-color="var(--photo-a)"/><stop offset=".55" stop-color="#4a423f"/><stop offset="1" stop-color="var(--photo-b)"/>
      </linearGradient>
      <linearGradient id="navyFade" x1="0" y1="0" x2="1" y2="0">
        <stop offset="0" stop-color="var(--navy-deep)"/><stop offset="1" stop-color="var(--blue)"/>
      </linearGradient>
    </defs>
    <rect width="508" height="725" fill="url(#frontTop)"/>
    <polygon points="0,105 105,0 160,0 0,160" fill="var(--red)"/>
    <polygon role="img" aria-label="Photo of commuters packed tightly inside a UK train carriage" points="0,430 508,205 508,478 0,700" fill="url(#trainCrowd)"/>
    <polygon points="0,330 508,175 508,205 0,430" fill="var(--red)"/>
    <polygon points="0,395 508,190 508,205 0,430" fill="var(--red-dark)" opacity=".6"/>
    <polygon points="0,690 508,468 508,478 0,700" fill="var(--white)"/>
    <polygon points="0,700 508,478 508,725 0,725" fill="url(#navyFade)"/>
  </svg>

  <div class="abs corner-ribbon-text">No claim no fee!</div>

  <div class="abs cap-block">
    <div class="small">max of</div>
    <div class="amount">£300</div>
    <div class="small">per month.</div>
    <div class="tickets">on Weekly,<br>Monthly and<br>yearly ticket.</div>
  </div>

  <div class="abs brand">
    <div class="brand-dot"></div>
    <div class="brand-name">FERROLIX</div>
  </div>

  <div class="abs headline">Don't be short changed</div>
  <div class="abs band-line">It's your money get it back!!</div>

  <div class="abs deal-badge">
    <div class="title">THE BIG DEAL</div>
    <div class="sub">GET UP TO</div>
    <div class="pct">40<span>%</span></div>
    <div class="tail">OF COST OF<br>TICKET BACK</div>
  </div>

  <div class="abs comp-head"><b>Compensation</b><br>can be between</div>
  <div class="abs comp-box comp-box--low">50<small>%</small></div>
  <div class="abs comp-to">to</div>
  <div class="abs comp-box comp-box--high">100<small>%</small></div>
  <div class="abs comp-foot">the cost of a daily ticket</div>
</section>

<section class="page page--back">
  <svg class="shapes" width="508" height="725" viewBox="0 0 508 725">
    <defs>
      <linearGradient id="platformFade" x1="0" y1="0" x2="1" y2="0">
        <stop offset="0" stop-color="#ffffff" stop-opacity="0"/><stop offset=".45" stop-color="var(--photo-c)" stop-opacity=".55"/><stop offset="1" stop-color="#7a7f88"/>
      </linearGradient>
      <linearGradient id="stationCrowd" x1="0" y1="0" x2="0" y2="1">
        <stop offset="0" stop-color="#8e949c"/><stop offset=".45" stop-color="#4d4a4c"/><stop offset="1" stop-color="#2a2629"/>
      </linearGradient>
    </defs>
    <rect width="508" height="725" fill="#ffffff"/>
    <rect role="img" aria-label="Faded photo of a crowded station platform beside a stopped train" x="160" y="0" width="348" height="262" fill="url(#platformFade)"/>
    <rect role="img" aria-label="Photo of commuters stranded outside a busy UK station entrance" x="0" y="280" width="508" height="272" fill="url(#stationCrowd)"/>
    <polygon points="0,240 508,252 508,290 0,330" fill="var(--red)"/>
    <polygon points="0,312 508,278 508,290 0,330" fill="var(--red-dark)" opacity=".6"/>
    <polygon points="0,700 508,712 508,725 0,725" fill="var(--navy)"/>
  </svg>

  <div class="abs back-headline">We help train commuter<br>who pay very high price<br>for their rail ticket.</div>
  <div class="abs speech">on Weekly, Monthly and yearly ticket<br>get some of their money back when<br>their train is delayed or cancelled up<br>to a max of <em>£300 per month</em></div>

  <div class="abs band-copy">The get back up to 40% the cost of your ticket.</div>

  <div class="abs perk" style="left:26px;top:296px">No claim<br>no fee!!</div>
  <div class="abs perk" style="left:126px;top:288px">Unlimited<br>claims !!</div>
  <div class="abs perk" style="left:222px;top:282px">No form<br>filling</div>
  <div class="abs perk" style="left:326px;top:276px">No printing<br>no posting</div>

  <div class="abs closing">We do all the work just claim and wait for<br>your money through the post.</div>
  <div class="abs how-to">All you need to do is download our app<br>from the app store app or android of<br>visit our website <a href="#">www.ferrolix-example.com</a></div>
  <div class="abs store-slot store-slot--ios"></div>
  <div class="abs store-slot store-slot--android"></div>

  <div class="abs brand brand-small">
    <div class="brand-dot"></div>
    <div class="brand-name">FERROLIX</div>
  </div>
</section>

</body>
</html>
```